The Velorind Project

All information regarding the design is located at Velorind.com. Any questions regarding the project, will be answered on the site.

```html
<!DOCTYPE html>
<html lang="en">
<head>
<meta charset="utf-8">
<title>Velorind</title>
<link rel="stylesheet" href="https://fonts.googleapis.com/css2?family=PT+Sans:wght@400;700&display=swap">
<style>
  :root {
    --purple-top: #8b2f98;
    --purple-bottom: #5c1d68;
    --purple-deep: #4e1b5a;
    --purple-text: #5a1f6a;
    --brand: #4f2275;
    --white: #ffffff;
    --haze: #e7e5ea;
    --footer-bg: #f9f9f9;
    --footer-line: #ececec;
    --footer-text: #a9a9a9;
  }
  * { box-sizing: border-box; margin: 0; padding: 0; }
  html, body {
    width: 1200px; height: 706px; overflow: hidden;
    background: var(--white);
    font-family: "PT Sans", Tahoma, sans-serif;
  }
  .page { position: relative; width: 1200px; height: 706px; }

  .topbar {
    position: absolute; left: 0; top: 0; width: 1200px; height: 45px;
    background: linear-gradient(to bottom, var(--purple-top), var(--purple-bottom));
  }
  .main-nav { position: absolute; left: 0; top: 0; height: 45px; }
  .main-nav a {
    position: absolute; top: 13px; color: var(--white);
    font-size: 14px; text-decoration: none; text-transform: uppercase; white-space: nowrap;
  }
  .login-button {
    position: absolute; left: 1109px; top: 8px; width: 76px; height: 26px;
    background: linear-gradient(to bottom, #ffffff, #e2dde6);
    border: 1px solid #c9b9d2;
    color: var(--purple-text); font-size: 13px; line-height: 24px; text-align: center;
  }

  .haze {
    position: absolute; left: 0; top: 45px; width: 1200px; height: 90px;
    background: linear-gradient(to bottom, var(--haze), var(--white));
  }

  .brand {
    position: absolute; left: 0; top: 232px; width: 1200px; text-align: center;
    font-size: 56px; color: var(--brand); line-height: 1; letter-spacing: 1px;
  }

  .search-panel {
    position: absolute; left: 282px; top: 313px; width: 641px; height: 78px;
    border-radius: 4px;
    background: linear-gradient(to bottom, #7a2a88, var(--purple-deep));
    box-shadow: 0 10px 14px -8px rgba(0,0,0,0.35);
  }
  .search-input {
    position: absolute; left: 25px; top: 22px; width: 523px; height: 34px;
    background: linear-gradient(to bottom, #f1eef3, #ffffff 45%);
    color: var(--purple-text); font-size: 14px; line-height: 34px; padding-left: 14px;
  }
  .search-go {
    position: absolute; left: 557px; top: 22px; width: 58px; height: 34px;
    background: linear-gradient(to bottom, #ffffff, #dcc1ef);
    color: var(--purple-text); font-size: 17px; font-weight: 700;
    line-height: 34px; text-align: center;
  }

  .footer {
    position: absolute; left: 0; top: 660px; width: 1200px; height: 46px;
    background: var(--footer-bg); border-top: 1px solid var(--footer-line);
    color: var(--footer-text); font-size: 11px;
  }
  .footer span { position: absolute; top: 18px; white-space: nowrap; }
</style>
</head>
<body>
<div class="page">
  <header class="topbar">
    <nav class="main-nav">
      <a style="left:14px">Web</a>
      <a style="left:75px">Images</a>
      <a style="left:154px">Videos</a>
      <a style="left:232px">News</a>
      <a style="left:301px">Maps</a>
    </nav>
    <div class="login-button">LOGIN</div>
  </header>
  <div class="haze"></div>

  <h1 class="brand">Velorind</h1>

  <form class="search-panel">
    <div class="search-input">Ask your question here</div>
    <div class="search-go">GO</div>
  </form>

  <footer class="footer">
    <span style="left:15px">Copyright © 2013 Velorind. All rights reserved</span>
    <span style="left:920px">Privacy Policy</span>
    <span style="left:1004px">|</span>
    <span style="left:1026px">Terms of use</span>
  </footer>
</div>
</body>
</html>
```